Label Design for Climbing Chalk (fitness category)

I am looking for someone to design a front and back label for a bottle of liquid chalk. Liquid chalk is used in gyms, gymnastics, climbing to prevent your hands from getting moist and increase friction. I'm uploading some design motivations that I like.

The bottle is going to be black and I want the label to be clear. You have free reign of how you want to approach this design. Below are more specifics for the sizing:

*Attached is a picture of a competitor product (Tor Hold Liquid Chalk). Please don't use this for motivation, their label is very bad. I'm attaching a picture so that you can see what the bottle looks like.
*Attached are design motivations that I like
*The bottle is 50 ml, it's 3.75 inches tall, 2 inches wide and 1.25 inches in depth.
*The label can be square or oval (it's up to you). The size of the label needs to be 1,25 x 2.25 inches.
*Name of the product: Varnel Liquid Chalk
*Label needs to have the following Required Text. You can arrange it however you like:
- (50 ml)
- Made by USA Competitive Athletes for Athletes. Increases grip and lasts 3-4 times longer than regular chalk.
- Directions: Shake well. Squeeze some Varnel Liquid Chalk into your hand and rub your hands together. Let your hands air dry for about 10 seconds. To remove the chalk wash your hands with light soap.
Warning: Avoid contact with Eyes. Do not use on broken skin. Do not ingest. Keep out of reach of small children.
- Ingredients: Magnesium carbonate, SD Alcohol, hydroxypropylcellulose, colophonium.

Target Market(s)

Fitness, Athletes, Rock Climbers, Weight Lifters, Gymnasts, etc

Industry/Entity Type

Fitness

Font styles to use
Sans Serif

Colors

Designer to choose colors to be used in the design.

Requirements
Must have
• Please see Project Description for required text. The bottle is going to be black and I want the clear label so please be creative with the colors that would look good
Nice to have
• Please see attached branding ideas that I liked for font and colors. You don't have to strictly stick to them, these are just some of the ones I liked. Be creative and put your best foot forward.

```html
<!DOCTYPE html>
<html lang="en">
<head>
<meta charset="utf-8">
<title>Varnel Liquid Chalk – Front and Back Labels</title>
<link rel="stylesheet" href="https://fonts.googleapis.com/css2?family=Barlow+Condensed:wght@400;500;700&family=Barlow+Semi+Condensed:wght@700&display=swap">
<style>
  :root {
    --orange: #f0542a;
    --red: #e4312a;
    --label-black: #0c0c0c;
    --panel-grey: #2a2a2a;
    --white: #ffffff;
    --page: #e6e6e6;
    --divider: #8a8a8a;
  }
  * { box-sizing: border-box; margin: 0; padding: 0; }
  html, body {
    width: 1200px; height: 873px; overflow: hidden;
    background: var(--page);
    font-family: "Barlow Condensed", "Arial Narrow", sans-serif;
    color: var(--white);
  }
  .sheet {
    width: 1200px; height: 873px;
    display: flex; justify-content: center; align-items: center; gap: 60px;
  }
  .label {
    position: relative;
    width: 420px; height: 780px;
    background: var(--label-black);
    border: 3px solid var(--orange);
    border-radius: 22px 22px 50% 50% / 22px 22px 27% 27%;
    overflow: hidden;
  }
  .label__top { position: absolute; left: 0; right: 0; top: 0; height: 505px; }
  .chalk-burst {
    position: absolute; left: 60px; right: 60px; bottom: 0; height: 120px;
    background: radial-gradient(ellipse 55% 70% at 50% 100%, rgba(255,255,255,.85) 0%, rgba(220,220,220,.35) 40%, rgba(12,12,12,0) 75%);
  }
  .brand-name {
    font-family: "Barlow Condensed", "Arial Narrow", sans-serif;
    font-weight: 700; color: var(--red); text-transform: uppercase; line-height: .9;
  }
  .label--front .brand-name { position: absolute; left: 44px; top: 50px; width: 330px; }
  .label--front .brand-name__main { display: block; font-size: 118px; letter-spacing: 1px; }
  .label--front .brand-name__sub { display: block; font-size: 56px; margin-top: 14px; }
  .brand-mark {
    position: absolute; left: 48px; top: 340px; width: 26px; height: 26px;
    background: var(--red);
  }
  .label--back .brand-name { position: absolute; left: 36px; top: 40px; width: 350px; }
  .label--back .brand-name__main { display: block; font-size: 64px; }
  .label--back .brand-name__sub { display: block; font-size: 34px; margin-top: 6px; }
  .usage-copy {
    position: absolute; left: 36px; right: 30px; top: 190px;
    font-size: 21.5px; line-height: 1.1; font-weight: 400;
  }
  .usage-copy p + p { margin-top: 10px; }
  .usage-copy strong { color: var(--orange); font-weight: 500; }
  .sport-band {
    position: absolute; left: 0; right: 0; top: 505px; height: 34px;
    background: var(--orange);
    display: flex; align-items: center; justify-content: center; gap: 8px;
    font-family: "Barlow Semi Condensed", "Arial Narrow", sans-serif;
    font-weight: 700; font-size: 19px; letter-spacing: 1.5px; color: var(--white);
  }
  .sport-band__dot { width: 7px; height: 7px; border-radius: 50%; background: var(--label-black); }
  .label__bottom {
    position: absolute; left: 0; right: 0; top: 539px; bottom: 0;
    background: var(--panel-grey);
  }
  .claims {
    position: absolute; left: 0; right: 0; top: 26px;
    display: flex; justify-content: center;
    font-size: 24px; line-height: 1.22;
  }
  .claims__maker { width: 172px; text-align: right; padding-right: 12px; border-right: 1px solid var(--divider); }
  .claims__maker em { font-style: normal; color: var(--orange); }
  .claims__benefit { width: 172px; padding-left: 12px; }
  .ingredients {
    position: absolute; left: 40px; right: 40px; top: 30px;
    text-align: center; font-size: 21.5px; line-height: 1.1;
  }
  .ingredients h3 { color: var(--orange); font-weight: 700; font-size: 22px; }
  .volume-tab {
    position: absolute; left: 50%; bottom: -3px; transform: translateX(-50%);
    width: 112px; height: 50px;
    background: var(--orange);
    border-radius: 56px 56px 0 0;
    display: flex; align-items: center; justify-content: center; padding-top: 4px;
    font-weight: 700; font-size: 25px; color: var(--white);
  }
</style>
</head>
<body>
<main class="sheet">

  <section class="label label--front" aria-label="Front label">
    <div class="label__top">
      <h1 class="brand-name">
        <span class="brand-name__main">Varnel</span>
        <span class="brand-name__sub">Liquid Chalk</span>
      </h1>
      <span class="brand-mark"></span>
      <div class="chalk-burst" role="img" aria-label="Burst of white chalk dust"></div>
    </div>
    <div class="sport-band">
      <span>Gym</span><span class="sport-band__dot"></span><span>Gymnastic</span><span class="sport-band__dot"></span><span>Climbing</span>
    </div>
    <div class="label__bottom">
      <div class="claims">
        <p class="claims__maker">Made by<br><em>USA Competitive</em><br><em>Athletes</em> for<br>Athletes</p>
        <p class="claims__benefit">Increases grip &amp;<br>lasts 3-4 times<br>longer than<br>regular chalk</p>
      </div>
      <div class="volume-tab">50 ml</div>
    </div>
  </section>

  <section class="label label--back" aria-label="Back label">
    <div class="label__top">
      <h2 class="brand-name">
        <span class="brand-name__main">Varnel</span>
        <span class="brand-name__sub">Liquid Chalk</span>
      </h2>
      <div class="chalk-burst" role="img" aria-label="Burst of white chalk dust"></div>
      <div class="usage-copy">
        <p><strong>Directions:</strong> Shake well. Squeeze some Varnel Liquid Chalk into your hand and rub your hands together. Let your hands air dry for about 10 seconds. To remove the chalk wash your hands with light soap.</p>
        <p><strong>Warning:</strong> Avoid contact with Eyes. Do not use on broken skin. Do not ingest. Keep out of reach of small children.</p>
      </div>
    </div>
    <div class="sport-band">
      <span>Gym</span><span class="sport-band__dot"></span><span>Gymnastic</span><span class="sport-band__dot"></span><span>Climbing</span>
    </div>
    <div class="label__bottom">
      <div class="ingredients">
        <h3>Ingredients:</h3>
        <p>Magnesium carbonate, SD Alcohol, hydroxypropylcellulose, colophonium.</p>
      </div>
      <div class="volume-tab">50 ml</div>
    </div>
  </section>

</main>
</body>
</html>
```